Letterhead and Envelope for Mental Health Business

I need letterhead and envelope designs that will match my business cards. I am attaching a *.pds file of my business card so it can be matched.

Business

```html
<!DOCTYPE html>
<html lang="en">
<head>
<meta charset="utf-8">
<title>Birch Counseling — Letterhead</title>
<link rel="stylesheet" href="https://fonts.googleapis.com/css2?family=Roboto+Condensed:wght@400;700&display=swap">
<style>
  :root {
    --paper: #ffffff;
    --brand-blue: #1e56c8;
    --brand-green: #4f9f2f;
    --ink-grey: #4a5358;
    --band-text: #ffffff;
  }
  * { margin: 0; padding: 0; box-sizing: border-box; }
  html, body {
    width: 1200px;
    height: 900px;
    overflow: hidden;
    background: var(--paper);
  }
  .letterhead {
    position: relative;
    width: 1200px;
    height: 900px;
    background: var(--paper);
    font-family: "Roboto Condensed", "Arial Narrow", sans-serif;
  }
  .brand {
    position: absolute;
    left: 66px;
    top: 96px;
    display: flex;
    align-items: center;
    gap: 16px;
  }
  .brand-dot {
    width: 96px;
    height: 96px;
    border-radius: 50%;
    background: var(--brand-green);
    flex: none;
  }
  .brand-name {
    font-weight: 700;
    font-size: 46px;
    line-height: 1;
    color: var(--brand-blue);
    letter-spacing: 0.5px;
    white-space: nowrap;
  }
  .brand-web {
    position: absolute;
    left: 67px;
    top: 231px;
    font-weight: 700;
    font-size: 20px;
    letter-spacing: 3.1px;
    color: var(--ink-grey);
    white-space: nowrap;
  }
  .contact-band {
    position: absolute;
    left: 0;
    top: 731px;
    width: 1200px;
    height: 169px;
    background: var(--brand-blue);
  }
  .contact-item {
    position: absolute;
    top: 34px;
    font-weight: 400;
    font-size: 21px;
    letter-spacing: 2.4px;
    color: var(--band-text);
    white-space: nowrap;
  }
  .contact-address { left: 68px; }
  .contact-phone { left: 466px; }
  .contact-email { left: 783px; top: 31px; letter-spacing: 2px; }
</style>
</head>
<body>
  <main class="letterhead">
    <header class="brand">
      <span class="brand-dot" aria-hidden="true"></span>
      <span class="brand-name">Birch Counseling</span>
    </header>
    <p class="brand-web">WWW.BIRCHCOUNSELINGLLC.COM</p>

    <footer class="contact-band">
      <span class="contact-item contact-address">ELM STREET 45, 1234 NY, USA</span>
      <span class="contact-item contact-phone">PHONE: 555/014-0199</span>
      <span class="contact-item contact-email">hello@birchcounselingllc.com</span>
    </footer>
  </main>
</body>
</html>
```